VantoMedix website

I have a plumfield hosting website already & have been using wordpress.
See www.vantomedix-sample.com
I have a logo's already.
I need a front page "VantoMedix". I have 3 products: (need separate pages)
1) the "GlideTray" (can't supply images ATM)
2) the "TubeKeeper" (several stills below & animation: http://www.clipvault-example.com/watch?v=Z7HqR20mW3x&list=QPtr8B_kzoepWnXcM4Lq5B_T&feature=share)
3) the "FastPart" animation here: http://clipv.example/pwrtk-Mmo_E & logo as below

It needs to be corporate & professional looking. VantoMedix is an innovative design house for medical devices.

Reason: Hi Designers, thanks for all your work to date - there have been some great designs. We'll be providing feedback to some of you in the near future. The reason we have extended the deadline is simply that we are too busy with other aspects of the business to focus on this at the moment. Kind regards, the VantoMedix team.

Dear Designers,

VantoMedix apologies for the delay due to our busyness. 
Please help us to understand the process here:
are we getting fully working websites? With multiple pages? Will we be able to modify them?
If not, what is the output?

Kind regards,
the Vanto team.

```html
<!DOCTYPE html>
<html lang="en">
<head>
<meta charset="utf-8">
<title>VantoMedix</title>
<link href="https://fonts.googleapis.com/css2?family=Montserrat:wght@400;600;700&family=Mulish:wght@400;600;700&display=swap" rel="stylesheet">
<style>
:root{
  --hero:#a2e1fb;
  --hero-light:#d9f4fe;
  --page:#e4f5fd;
  --blue:#1f95d6;
  --blue-head:#2aa6e0;
  --blue-bright:#3fb5ea;
  --orange:#f2620f;
  --orange-light:#ff8a2e;
  --green:#4aa81f;
  --text:#3d4650;
  --muted:#9aa3ab;
  --nav:#8a949c;
  --white:#fff;
  --line:#d5dde3;
}
*{margin:0;padding:0;box-sizing:border-box}
html,body{width:1085px;height:1200px;overflow:hidden}
body{position:relative;background:var(--page);font-family:"Mulish",Arial,sans-serif;color:var(--text)}
.abs{position:absolute}
.hero-bg{left:0;top:0}
.logo{left:142px;top:28px;font-family:"Montserrat",Arial,sans-serif;font-weight:700;font-size:46px;color:var(--blue);letter-spacing:-1px;display:flex;align-items:center;gap:10px}
.logo .dot{width:16px;height:16px;border-radius:50%;background:var(--orange)}
.social{top:41px;width:27px;height:27px;border-radius:2px}
.social.s1{left:557px;background:#3a5a98}
.social.s2{left:598px;background:#2eaee3}
.social.s3{left:638px;background:#1d6fa5}
.call{left:684px;top:43px;display:flex;align-items:center;gap:7px;font-family:"Montserrat",Arial,sans-serif;font-weight:600;font-size:19px;color:var(--orange)}
.nav{left:142px;top:108px;width:799px;height:42px;background:var(--white);box-shadow:0 1px 3px rgba(0,0,0,.12);display:flex;align-items:center;font-family:"Montserrat",Arial,sans-serif;font-weight:600;font-size:11.5px;color:var(--nav)}
.nav span{padding:0 20px;height:100%;display:flex;align-items:center;border-right:1px solid #eef1f3}
.nav .active{background:var(--blue-head);color:var(--white);width:80px;justify-content:center;padding:0}
.nav span:nth-child(2){border-right:none}
.photo{left:632px;top:112px;width:283px;height:424px;border-radius:140px 140px 0 0;background:linear-gradient(180deg,#c9a88e 0%,#3a8fd8 28%,#2f7fcf 100%)}
.kicker{left:154px;top:231px;font-family:"Montserrat",Arial,sans-serif;font-weight:700;font-size:13px;color:var(--blue)}
.headline{left:153px;top:253px;width:440px;font-family:"Montserrat",Arial,sans-serif;font-weight:600;font-size:23.5px;line-height:30.5px;color:var(--white);text-shadow:0 1px 3px rgba(0,80,130,.35)}
.btn{display:flex;align-items:center;justify-content:center;background:linear-gradient(180deg,var(--orange-light),var(--orange));color:var(--white);font-family:"Montserrat",Arial,sans-serif;font-weight:600;border-radius:2px;box-shadow:0 1px 2px rgba(0,0,0,.2)}
.btn.learn{left:154px;top:382px;width:119px;height:38px;font-size:13px}
.card{top:581px;width:184px;height:295px;background:var(--white);box-shadow:0 1px 3px rgba(0,0,0,.12)}
.card-head{height:58px;background:linear-gradient(180deg,var(--blue-bright),var(--blue-head));color:var(--white);font-family:"Montserrat",Arial,sans-serif;font-weight:600;font-size:13px;display:flex;align-items:center;padding-left:17px}
.card-head.center{justify-content:center;padding-left:0;font-size:15px;letter-spacing:.5px}
.thumb{margin:18px 0 0 11px;width:160px;height:108px;border-radius:3px}
.t1{background:linear-gradient(135deg,#b8b8e8,#8f93d2)}
.t2{background:linear-gradient(180deg,#ffffff,#e7e7ea 80%,#222 80%)}
.t3{background:linear-gradient(180deg,#6a4a3e,#4a2f2a 80%,#111 80%)}
.card p{margin:20px 14px 0 14px;font-size:10.5px;line-height:15.3px;color:var(--muted)}
.read{margin:14px 0 0 14px;display:inline-block;font-family:"Montserrat",Arial,sans-serif;font-weight:700;font-size:9px;color:var(--blue);border-bottom:1px solid var(--blue)}
.contact-info{padding:16px 16px 0;font-size:10.5px;color:var(--muted);line-height:24.5px}
.contact-info a{color:var(--blue);text-decoration:none}
.contact-info .gap{height:13px}
.btn.contact{left:28px;top:231px;width:119px;height:38px;font-size:13px}
.footer{left:0;top:895px;width:1085px;height:248px;background:var(--white);border-top:1px solid var(--line);border-bottom:1px solid var(--line)}
.col{top:32px;width:190px;font-size:10.8px;line-height:18px;color:var(--text)}
.col h3{font-family:"Montserrat",Arial,sans-serif;font-weight:700;font-size:12px;color:var(--blue-head);margin-bottom:9px}
.tag{color:#e8452a}
.ago{color:var(--muted);font-style:italic;margin-bottom:9px}
.input{margin-top:9px;width:187px;height:29px;border:1px solid #dbe1e5;background:#f7f8f9;font-size:10px;color:var(--muted);display:flex;align-items:center;padding-left:8px}
.signup{margin-top:14px;width:78px;height:30px;background:linear-gradient(180deg,#5cbf2a,var(--green));color:var(--white);font-family:"Montserrat",Arial,sans-serif;font-weight:700;font-size:10.5px;display:flex;align-items:center;justify-content:center;border-radius:2px}
.navcols{display:flex;gap:48px}
.navcols div{line-height:22px}
.copy{left:142px;top:1162px;font-size:10.5px;color:var(--muted)}
.legal{right:144px;top:1162px;font-family:"Montserrat",Arial,sans-serif;font-weight:600;font-size:10px;color:#8aa0ae}
</style>
</head>
<body>
<svg class="abs hero-bg" width="1085" height="545" viewBox="0 0 1085 545" aria-hidden="true">
  <defs>
    <radialGradient id="glow" cx="0.2" cy="0.05" r="0.55">
      <stop offset="0" stop-color="#ecfaff"/>
      <stop offset="1" stop-color="#a2e1fb"/>
    </radialGradient>
  </defs>
  <path d="M0,0 H1085 V449 Q542,631 0,449 Z" fill="url(#glow)"/>
</svg>

<div class="abs logo"><span class="dot"></span>VantoMedix</div>
<div class="abs social s1"></div>
<div class="abs social s2"></div>
<div class="abs social s3"></div>
<div class="abs call">
  <svg width="20" height="20" viewBox="0 0 24 24" aria-hidden="true"><path d="M6.6 10.8a15 15 0 006.6 6.6l2.2-2.2c.3-.3.7-.4 1-.2 1.1.4 2.3.6 3.6.6.6 0 1 .4 1 1V20c0 .6-.4 1-1 1A17 17 0 013 4c0-.6.4-1 1-1h3.5c.6 0 1 .4 1 1 0 1.3.2 2.5.6 3.6.1.3 0 .7-.2 1z" fill="#6fb3e0"/></svg>
  CALL US +1800.555.0199
</div>

<div class="abs photo" role="img" aria-label="Photo of a smiling nurse in blue scrubs with a stethoscope, arms crossed"></div>

<nav class="abs nav">
  <span class="active">HOME</span>
  <span>PRODUCTS</span>
  <span>ABOUT US</span>
  <span>ASK QUESTION</span>
  <span>CONTACT US</span>
</nav>

<div class="abs kicker">DID YOU KNOW?</div>
<div class="abs headline">Two thirds of injuries to paramedics affect the back and come from lifting and carrying?</div>
<div class="abs btn learn">Learn More</div>

<div class="abs card" style="left:147px">
  <div class="card-head">GlideTray</div>
  <div class="thumb t1" role="img" aria-label="Render of the GlideTray device"></div>
  <p>Lorem ipsum dolor sit amet, consectetur adipisicing elit, sed do eiusmod tempor incididunt</p>
  <span class="read">READ MORE</span>
</div>
<div class="abs card" style="left:350px">
  <div class="card-head center">TubeKeeper</div>
  <div class="thumb t2" role="img" aria-label="Video still of the TubeKeeper animation"></div>
  <p>Lorem ipsum dolor sit amet, consectetur adipisicing elit, sed do eiusmod tempor incididunt</p>
  <span class="read">READ MORE</span>
</div>
<div class="abs card" style="left:551px">
  <div class="card-head center">FastPart</div>
  <div class="thumb t3" role="img" aria-label="Video still of the FastPart animation"></div>
  <p>Lorem ipsum dolor sit amet, consectetur adipisicing elit, sed do eiusmod tempor incididunt</p>
  <span class="read">READ MORE</span>
</div>
<div class="abs card" style="left:754px">
  <div class="card-head">Questions? Contact us!</div>
  <div class="contact-info">
    <div>Phone: (+39) 0200 555 018</div>
    <div>E-mail: <a>info@vantomedix-sample.com</a></div>
    <div class="gap"></div>
    <div>Harbor Lane, Company Inc.</div>
    <div>4471 Elm Avenue</div>
    <div>Portland, USA</div>
  </div>
  <div class="abs btn contact">Contact Us</div>
</div>

<footer class="abs footer">
  <div class="abs col" style="left:143px">
    <h3>ABOUT</h3>
    <div>Donec rutrum elit ac arcu bibendum rhoncus in vitae turpis. Quisque fermentum gravida eros non faucibus. Curabitur fermentum, arcu sed cursus commodo.</div>
    <div style="margin-top:9px;line-height:20px">hello@vantomedix-sample.com<br>+1 (555) 010 - 42 - 87</div>
  </div>
  <div class="abs col" style="left:347px;width:180px">
    <h3>RECENT TWEETS</h3>
    <div><span class="tag">@vantomedix</span> Vivamus porta dui dapibus erat egestas semper. In quis sem neque <span class="tag">#paramedic #vanto</span></div>
    <div class="ago">5 minutes ago</div>
    <div><span class="tag">@vantomedix</span> Vivamus porta dui dapibus erat egestas semper. In quis sem neque <span class="tag">#paramedic #vanto</span></div>
    <div class="ago">1 day ago</div>
  </div>
  <div class="abs col" style="left:550px">
    <h3>NEWSLETTER SIGNUP</h3>
    <div>Donec rutrum elit ac arcu bibendum rhoncus in vitae turpis.</div>
    <div class="input">Enter your e-mail address</div>
    <div class="signup">SIGNUP</div>
  </div>
  <div class="abs col" style="left:754px">
    <h3>NAVIGATION</h3>
    <div class="navcols">
      <div>Home<br>Products<br>About Us<br>Ask Question<br>Contact Us</div>
      <div>GlideTray<br>TubeKeeper<br>FastPart</div>
    </div>
  </div>
</footer>

<div class="abs copy">Copyright © 2014 VantoMedix. All rights reserved.</div>
<div class="abs legal">Terms &amp; Conditions &nbsp;/&nbsp; Privacy Policy &nbsp;/&nbsp; FAQ</div>
</body>
</html>
```